Business Card for Quillmark Ledger - A cannabis publication for executives.

I'd like some business cards for Quillmark Ledger. The logo is done (great job!) and I need a card design I will use with PRINTLY. I made it a short project to allow time for printing before an event. These will be standard sized cards (final artwork size 3.66" x 2.16" at 300dpi) with a final card size of 3.5" x 2.0". (See PRINTLY.com if you need more info.) I might try rounded corners but am not sure yet. I think the design will work okay with rounded.

Quillmark Ledger will be a bi-weekly publication for the cannabis industry. It is targeted to investors and industry executives, not consumers or pot smokers. So our market is more B2B. However I am open to creativity and making the card something people remark on.

My contact for card:

Dana Merrow
Founder/CEO
dana@quillmarkledger.example

2740 Harlow Avenue
Boston MA 02135
(617)555-0194

Target Market(s)

Executives, Industry people and investors in the Cannabis sector.

Contact Information for Business Card

PRINTLY does do double sided and the second side can be the same or different images. Only one side is required but use of the second side would be a bonus.

Font styles to use
Serif
Sans Serif
Decorative

Colors

Designer to choose colors to be used in the design.

Requirements
Must have
• Logo, contact info
Nice to have
• Style and design to make the card stand out in a crowd.

```html
<!DOCTYPE html>
<html lang="en">
<head>
<meta charset="utf-8">
<title>Quillmark Ledger — Business Card</title>
<link rel="stylesheet" href="https://fonts.googleapis.com/css2?family=Philosopher:wght@700&family=Titillium+Web:wght@400&display=swap">
<style>
  :root {
    --brand-blue: #1173bd;
    --brand-green: #72a52c;
    --card-white: #ffffff;
    --ink: #3b3b3b;
    --stage: #e6e7e9;
  }
  * { margin: 0; padding: 0; box-sizing: border-box; }
  html, body { width: 1200px; height: 1200px; overflow: hidden; }
  body {
    background: var(--stage);
    display: flex;
    flex-direction: column;
    align-items: center;
    justify-content: center;
    gap: 60px;
    font-family: "Titillium Web", sans-serif;
  }
  .card {
    position: relative;
    width: 700px;
    height: 400px;
    box-shadow: 0 6px 20px rgba(0,0,0,0.15);
  }
  .card-back {
    background: var(--brand-blue);
    display: flex;
    align-items: center;
    justify-content: center;
  }
  .card-back .wordmark {
    font-family: "Philosopher", sans-serif;
    font-weight: 700;
    font-size: 56px;
    color: var(--card-white);
  }
  .card-front { background: var(--card-white); }
  .front-logo {
    position: absolute;
    left: 44px;
    top: 62px;
    display: flex;
    align-items: center;
    gap: 18px;
  }
  .front-logo .mark {
    width: 52px;
    height: 52px;
    background: var(--brand-green);
  }
  .front-logo .wordmark {
    font-family: "Philosopher", sans-serif;
    font-weight: 700;
    font-size: 44px;
    color: var(--brand-blue);
  }
  .identity {
    position: absolute;
    right: 60px;
    top: 178px;
    text-align: right;
  }
  .identity .person-name {
    font-family: "Philosopher", sans-serif;
    font-weight: 700;
    font-size: 36px;
    line-height: 1.1;
    color: var(--brand-green);
  }
  .identity .person-title {
    font-size: 20px;
    color: var(--ink);
  }
  .accent-bar {
    position: absolute;
    right: 20px;
    top: 180px;
    width: 22px;
    height: 76px;
    background: var(--brand-blue);
  }
  .contact {
    position: absolute;
    left: 50px;
    bottom: 32px;
    padding-left: 14px;
    border-left: 2px solid var(--brand-blue);
    list-style: none;
    font-size: 20px;
    color: var(--ink);
    line-height: 1.35;
  }
  .contact li { display: flex; align-items: flex-start; gap: 8px; }
  .contact li + li { margin-top: 4px; }
  .contact svg { flex: none; width: 18px; height: 18px; margin-top: 5px; fill: var(--brand-blue); }
</style>
</head>
<body>
  <section class="card card-back" aria-label="Card back">
    <span class="wordmark">Quillmark Ledger</span>
  </section>

  <section class="card card-front" aria-label="Card front">
    <div class="front-logo">
      <span class="mark"></span>
      <span class="wordmark">Quillmark Ledger</span>
    </div>

    <div class="identity">
      <p class="person-name">Dana Merrow</p>
      <p class="person-title">Founder/CEO</p>
    </div>
    <span class="accent-bar"></span>

    <ul class="contact">
      <li>
        <svg viewBox="0 0 24 24" aria-hidden="true"><path d="M2 9c0-3 4-5 10-5s10 2 10 5v2h-5V8.5c-1.5-.5-3-.7-5-.7s-3.5.2-5 .7V11H2z"/><path d="M6 12h12l2 8H4z"/><circle cx="12" cy="16" r="2" fill="#fff"/></svg>
        <span>(617)555-0194</span>
      </li>
      <li>
        <svg viewBox="0 0 24 24" aria-hidden="true"><path d="M2 5h20v14H2z"/><path d="M2 5l10 8 10-8" fill="none" stroke="#fff" stroke-width="2"/></svg>
        <span>dana@quillmarkledger.example</span>
      </li>
      <li>
        <svg viewBox="0 0 24 24" aria-hidden="true"><path d="M12 1a8 8 0 0 0-8 8c0 6 8 14 8 14s8-8 8-14a8 8 0 0 0-8-8zm0 11a3 3 0 1 1 0-6 3 3 0 0 1 0 6z"/></svg>
        <span>2740 Harlow Avenue<br>Boston MA 02135</span>
      </li>
    </ul>
  </section>
</body>
</html>
```